Online video and marketing company business cards

Need to get some new business cards designed to fit with our new logo. The cards should be professional, clean and simple.

Cards should have:

Name
Position
2 line address
telephone
mobile
email address
web address

We need to have our logo and if possible say what we do...
ONLINE FILM PRODUCTION & STRATEGY

Industry/Entity Type

Marketing

```html
<!DOCTYPE html>
<html lang="en">
<head>
<meta charset="utf-8">
<title>Lumareel business card</title>
<link href="https://fonts.googleapis.com/css2?family=Barlow:wght@400;500;700&display=swap" rel="stylesheet">
<style>
  :root {
    --backdrop: #e4e5e7;
    --card-body: #6aa7c4;
    --navy: #1b4b7f;
    --cyan: #0090bf;
    --white: #ffffff;
  }
  html, body {
    margin: 0;
    width: 1096px;
    height: 1200px;
    overflow: hidden;
    background: var(--backdrop);
    font-family: "Barlow", Arial, sans-serif;
  }
  .stage {
    width: 1096px;
    height: 1200px;
    display: flex;
    align-items: center;
    justify-content: center;
  }
  .card {
    position: relative;
    width: 980px;
    height: 560px;
    background: var(--card-body);
    overflow: hidden;
    box-shadow: 0 10px 30px rgba(0,0,0,0.12);
  }
  .band {
    position: absolute;
    left: 0;
    width: 100%;
    height: 30px;
    display: flex;
  }
  .band span { flex: 1; }
  .band--top { top: 0; }
  .band--bottom { bottom: 0; }
  .band .navy { background: var(--navy); }
  .band .cyan { background: var(--cyan); }
  .band span + span { border-left: 4px solid var(--card-body); }

  .brand {
    position: absolute;
    left: 70px;
    top: 62px;
    display: flex;
    align-items: center;
    gap: 22px;
  }
  .brand__dot {
    width: 66px;
    height: 66px;
    border-radius: 50%;
    background: var(--navy);
  }
  .brand__name {
    font-size: 104px;
    font-weight: 700;
    color: var(--navy);
    line-height: 1;
    letter-spacing: -1px;
  }

  .icon-tab {
    position: absolute;
    left: 0;
    top: 232px;
    width: 102px;
    bottom: 30px;
    background: var(--white);
    border-radius: 0 18px 0 0;
  }
  .icon-tab svg {
    position: absolute;
    left: 38px;
    width: 28px;
    height: 28px;
    fill: none;
    stroke: var(--navy);
    stroke-width: 2.2;
  }
  .icon-tab .solid { fill: var(--navy); stroke: none; }

  .contact {
    position: absolute;
    left: 132px;
    top: 240px;
    margin: 0;
    padding: 0;
    list-style: none;
    color: var(--white);
    font-size: 25px;
    line-height: 36px;
    font-weight: 400;
  }
  .contact .phones { display: flex; align-items: center; gap: 14px; }
  .contact .mobile-icon { width: 18px; height: 26px; }

  .name-tag {
    position: absolute;
    right: 0;
    top: 318px;
    width: 330px;
    height: 120px;
    background: var(--white);
    border-radius: 18px 0 0 18px;
    padding: 18px 0 0 30px;
    box-sizing: border-box;
    color: var(--navy);
  }
  .name-tag__name {
    font-size: 42px;
    font-weight: 500;
    line-height: 1;
    margin: 0;
  }
  .name-tag__role {
    font-size: 28px;
    font-weight: 400;
    margin: 10px 0 0 56px;
  }
</style>
</head>
<body>
<main class="stage">
  <article class="card">
    <div class="band band--top"><span class="navy"></span><span class="cyan"></span></div>
    <div class="band band--bottom"><span class="cyan"></span><span class="navy"></span></div>

    <header class="brand">
      <span class="brand__dot"></span>
      <span class="brand__name">lumareel</span>
    </header>

    <div class="icon-tab" aria-hidden="true">
      <svg style="top:14px" viewBox="0 0 28 28"><path class="solid" d="M14 2a8 8 0 0 0-8 8c0 6 8 16 8 16s8-10 8-16a8 8 0 0 0-8-8zm0 11a3 3 0 1 1 0-6 3 3 0 0 1 0 6z"/></svg>
      <svg style="top:84px" viewBox="0 0 28 28"><path class="solid" d="M7 3l4 5-2 3c1.5 3 4 5.5 7 7l3-2 5 4-3 4C13 24 4 15 3 6z"/></svg>
      <svg style="top:120px" viewBox="0 0 28 28"><rect x="3" y="6" width="22" height="16"/><path d="M3 6l11 9 11-9M3 22l8-8M25 22l-8-8"/></svg>
      <svg style="top:156px" viewBox="0 0 28 28"><circle cx="14" cy="14" r="11"/><ellipse cx="14" cy="14" rx="5" ry="11"/><path d="M3 14h22M5 8h18M5 20h18"/></svg>
    </div>

    <ul class="contact">
      <li>Your residentiol or commercial or office address</li>
      <li>in two line</li>
      <li class="phones">
        <span>(00) 00 0000</span>
        <svg class="mobile-icon" viewBox="0 0 18 26" aria-hidden="true"><rect x="2" y="1" width="14" height="24" rx="2" fill="none" stroke="#ffffff" stroke-width="2"/><rect x="5" y="4" width="8" height="14" fill="#ffffff"/></svg>
        <span>(00) 0000000000</span>
      </li>
      <li>info.support@yourwebsite.com</li>
      <li>www.yourwebsite.com</li>
    </ul>

    <section class="name-tag">
      <p class="name-tag__name">YOUR NAME</p>
      <p class="name-tag__role">Position</p>
    </section>
  </article>
</main>
</body>
</html>
```